Profesional personal website needs design and business card

I need a business card with my professional name as a logo "Marlo Vitality" for my business. I am a Wellness Coach, consultant and trainer. So it should be professional, wellness oriented and modern.

Target Market(s)

Private clients, governments, corporations. Luxury and high market.

Industry/Entity Type

Health And Wellness

Contact Information for Business Card

Marlo Vitality should be the logo

Colors

Designer to choose colors to be used in the design.

Requirements
Must have
• Marlo Vitality
• Name: Tomás Arribal
• Wellness Coach, Consultant & Trainer.
• Website: www.marlovitality.example
• Phone:
• Spain (+34) 612 480 397
• (USA) +1 (555) 318 2046
Nice to have
• The most important is the design of "Marlo Vitality", as this is going to be my personal brand logo. It should be professional, wellness, high end and actual.
Should not have
• no golds, no baroque style..

```html
<!DOCTYPE html>
<html lang="en">
<head>
<meta charset="utf-8">
<title>Marlo Vitality – Business Card</title>
<link href="https://fonts.googleapis.com/css2?family=Lato:wght@400;700;900&display=swap" rel="stylesheet">
<style>
  :root {
    --backdrop: #5f5f5f;
    --card: #050708;
    --accent: #1577cc;
    --ink: #ffffff;
    --muted: #c9ccd0;
  }
  * { box-sizing: border-box; margin: 0; padding: 0; }
  html, body {
    width: 1200px; height: 900px; overflow: hidden;
    background: var(--backdrop);
    font-family: "Lato", Arial, sans-serif;
  }
  .stage {
    width: 1200px; height: 900px;
    display: flex; flex-direction: column; align-items: center; justify-content: center;
    gap: 44px;
  }
  .card {
    width: 600px; height: 343px;
    background: var(--card);
    position: relative;
    box-shadow: 0 10px 28px rgba(0,0,0,.35);
  }
  /* front */
  .card--front { display: flex; align-items: center; justify-content: center; }
  .brand {
    display: flex; align-items: center; gap: 14px;
    font-weight: 900; letter-spacing: .02em; text-transform: uppercase;
  }
  .brand__dot { width: 14px; height: 14px; border-radius: 50%; background: currentColor; }
  .brand--front { color: var(--ink); font-size: 40px; }
  .brand--back { color: var(--accent); font-size: 24px; gap: 10px; }
  .brand--back .brand__dot { width: 10px; height: 10px; }
  /* back */
  .card--back { display: flex; }
  .back__identity {
    width: 50%; display: flex; flex-direction: column; align-items: center; justify-content: center;
    gap: 64px; padding-top: 30px;
  }
  .website { font-size: 15px; letter-spacing: .22em; color: var(--ink); }
  .website__domain { color: var(--accent); }
  .divider { width: 1.5px; background: var(--accent); margin: 96px 0 98px; }
  .back__contact {
    flex: 1; padding: 96px 0 0 30px;
  }
  .name { color: var(--accent); font-weight: 900; font-size: 30px; letter-spacing: -.01em; text-transform: uppercase; line-height: 1; }
  .role { color: var(--ink); font-size: 14px; margin: 8px 0 20px; }
  .contact-list { list-style: none; display: flex; flex-direction: column; gap: 5px; }
  .contact-list li { display: flex; align-items: center; gap: 10px; color: var(--muted); font-size: 13px; }
  .contact-list svg { width: 14px; height: 14px; fill: var(--accent); flex: none; }
</style>
</head>
<body>
<main class="stage">
  <section class="card card--front" aria-label="Card front">
    <div class="brand brand--front"><span class="brand__dot"></span>Marlo Vitality</div>
  </section>

  <section class="card card--back" aria-label="Card back">
    <div class="back__identity">
      <div class="brand brand--back"><span class="brand__dot"></span>Marlo Vitality</div>
      <p class="website">www.<span class="website__domain">marlovitality</span>.example</p>
    </div>
    <div class="divider"></div>
    <div class="back__contact">
      <h1 class="name">Tomás Arribal</h1>
      <p class="role">Wellness Coach, Consultant &amp; Trainer</p>
      <ul class="contact-list">
        <li>
          <svg viewBox="0 0 24 24" aria-hidden="true"><path d="M6.6 10.8a15.1 15.1 0 0 0 6.6 6.6l2.2-2.2a1 1 0 0 1 1-.25 11.4 11.4 0 0 0 3.6.57 1 1 0 0 1 1 1V20a1 1 0 0 1-1 1A17 17 0 0 1 3 4a1 1 0 0 1 1-1h3.5a1 1 0 0 1 1 1c0 1.25.2 2.45.57 3.57a1 1 0 0 1-.25 1z"/></svg>
          (+34) 612 480 397 (Spain)
        </li>
        <li>
          <svg viewBox="0 0 24 24" aria-hidden="true"><path d="M6.6 10.8a15.1 15.1 0 0 0 6.6 6.6l2.2-2.2a1 1 0 0 1 1-.25 11.4 11.4 0 0 0 3.6.57 1 1 0 0 1 1 1V20a1 1 0 0 1-1 1A17 17 0 0 1 3 4a1 1 0 0 1 1-1h3.5a1 1 0 0 1 1 1c0 1.25.2 2.45.57 3.57a1 1 0 0 1-.25 1z"/></svg>
          +1 (555) 318 2046 (USA)
        </li>
        <li>
          <svg viewBox="0 0 24 24" aria-hidden="true"><path d="M2 5h20v14H2z M2 5l10 8 10-8" fill="none" stroke="#1577cc" stroke-width="2"/></svg>
          info@marlovitality.example
        </li>
      </ul>
    </div>
  </section>
</main>
</body>
</html>
```